Audio Video Lighting Free Rummage Run

I would like a digital flyer created for a ‘rummage run’ event I will host 12/29 -12/31.
The concept: I work for and Audio, Video, and Lighting company and we have a lot of products in our warehouse that we cannot sale for one reason or another. Some of the items are new and some are old, some work and some do not. I am going to allow non-profit originations (Churches, Orphanages, shelters, ect.) come through our warehouse ‘rummage’ through our inventory and take what they need for free. There are several large ticket items TV’s, Digital Mixing Consoles, and Speakers that we will raffle off on Thursday the 31st; Some of the raffle items are Valued at $25,000. I would like to include some stock pictures of these times. I would like a ‘cool’ flyer created that informs people that the event happing so they will come out. I’ll do a write up too, but I don’t think that has to be included in the flyer; the flyer just need to look modern and get the highpoints out for informational purposes.
Who: KTR Works : www.ktrworks-demo.net – An AVL company that specializes in Design and Installation of professional equipment.
What: Rummage Run – I just think rummage run has a fun ring to it…
When: 930am – 230pm Monday 12/29/20 – Thursday 12/31/20
Where: KTR Warehouse 4920 County Rd 38 Cedar Bend AL 35990
Why: 2020 has been a hard year for so many and KTR wants to do our part to bless people that bless people! Jesus Christ has given us the gifts and abilities to create and manage work this year that we never thought possible; we want to share what we have with others. The Mission of KTR is “To provide sound and vision so the WORD can be communicated to the world! If you are a non-profit organization that has AVL needs, we encourage you to come and ‘rummage’ through our stuff. There are many items in the following Categories: Audio, Video, Lighting, and Computers.

here is a link to the $25K item
https://www.plovermixers-demo.com/item.html?ref=K7TQW

Target Market(s)

Non Profits, Church's, Orphanages, shelters, ect.

Industry/Entity Type

Audio

Font styles to use
Sans Serif

Requirements
Must have
• See description
Nice to have
• See description
Should not have
• Profanity, nudity

```html
<!DOCTYPE html>
<html lang="en">
<head>
<meta charset="utf-8">
<title>Rummage Run – KTR Works</title>
<link rel="stylesheet" href="https://fonts.googleapis.com/css2?family=Arimo:ital,wght@0,400;0,700;1,700&family=Pacifico&display=swap">
<style>
  :root {
    --night: #1b1638;
    --violet: #4a2f7a;
    --magenta: #8a3a8f;
    --amber: #d9a24a;
    --star-edge: #ffffff;
    --pink: #e64d78;
    --white: #ffffff;
    --soft: #d9d4ea;
  }
  * { margin: 0; padding: 0; box-sizing: border-box; }
  html, body { width: 870px; height: 1200px; overflow: hidden; background: var(--night); }
  .flyer {
    position: relative; width: 870px; height: 1200px; overflow: hidden;
    font-family: "Arimo", Arial, sans-serif; color: var(--white);
  }
  .stage-photo {
    position: absolute; inset: 0;
    background:
      radial-gradient(ellipse at 50% 45%, rgba(217,162,74,.45) 0%, rgba(138,58,143,.35) 35%, transparent 65%),
      linear-gradient(180deg, var(--violet) 0%, var(--night) 60%, #120e26 100%);
  }
  .venue-strip {
    position: absolute; left: 0; top: 0; width: 870px; height: 110px;
    background: linear-gradient(90deg, #2b1f4f 0%, #7a4a2e 30%, #2a3f7a 55%, #6b3a6f 80%, #a0733f 100%);
    opacity: .85;
  }
  .top-brand {
    position: absolute; top: 30px; left: 0; width: 100%;
    text-align: center; font-weight: 700; font-size: 30px; letter-spacing: 2px;
  }
  .hero-star { position: absolute; left: 0; top: 0; }
  .performer-photo {
    position: absolute; left: 360px; top: 720px; width: 150px; height: 120px; border-radius: 8px;
    background: radial-gradient(ellipse at 50% 40%, #f0c98a 0%, #7a4a6f 55%, rgba(40,25,70,0) 100%);
  }
  .event-title {
    position: absolute; left: 0; top: 370px; width: 870px;
    text-align: center; font-family: "Pacifico", cursive; font-weight: 400;
    font-size: 100px; line-height: 1.05; color: var(--pink);
    transform: rotate(-9deg);
  }
  .details > * { position: absolute; font-style: italic; font-weight: 700; white-space: nowrap; }
  .date-start { left: 40px; top: 828px; font-size: 44px; }
  .date-end { left: 40px; top: 878px; font-size: 44px; }
  .date-start small, .date-end small { font-size: 24px; }
  .raffle-tag { font-size: 20px; margin-left: 18px; }
  .raffle-items { left: 40px; top: 934px; font-size: 17px; }
  .raffle-value { left: 300px; width: 245px; top: 956px; font-size: 46px; text-align: right; }
  .hours { left: 40px; top: 1012px; font-size: 38px; }
  .venue-address { left: 40px; top: 1068px; font-size: 22px; line-height: 1.3; }
  .mixer-photo {
    position: absolute; left: 570px; top: 870px; width: 270px; height: 175px; border-radius: 10px;
    background: linear-gradient(160deg, #c9ccd4 0%, #4c5466 45%, #1d2330 100%);
    transform: skewX(-10deg);
  }
  .mixer-caption { position: absolute; left: 610px; top: 1080px; font-size: 16px; color: var(--soft); }
  .footer-brand { position: absolute; left: 0; top: 1122px; width: 870px; text-align: center; }
  .footer-name { font-weight: 700; font-size: 28px; }
  .footer-web { font-size: 15px; color: var(--soft); margin-top: 4px; }
</style>
</head>
<body>
<main class="flyer">
  <div class="stage-photo" role="img" aria-label="Concert stage with purple and amber lighting beams"></div>
  <div class="venue-strip" role="img" aria-label="Row of photos of installed audio, video and lighting venues"></div>
  <div class="top-brand">KTR</div>

  <svg class="hero-star" width="870" height="1200" viewBox="0 0 870 1200" aria-hidden="true">
    <defs>
      <radialGradient id="star-fill" cx="50%" cy="50%" r="60%">
        <stop offset="0%" stop-color="#fffaf0"/>
        <stop offset="70%" stop-color="#fbf1d8"/>
        <stop offset="100%" stop-color="#f1d9a6"/>
      </radialGradient>
    </defs>
    <polygon points="410,80 500,300 830,330 600,480 700,770 440,610 170,770 290,480 40,450 320,300"
      fill="url(#star-fill)" stroke="var(--star-edge)" stroke-width="10" stroke-linejoin="round"/>
  </svg>

  <div class="performer-photo" role="img" aria-label="Musician with guitar performing on a lit stage"></div>
  <h1 class="event-title">Rummage<br>Run</h1>

  <section class="details">
    <p class="date-start">12/29/20 <small>(Monday)</small> ~</p>
    <p class="date-end">12/31/20 <small>(Thursday)</small><span class="raffle-tag">Raffle Day</span></p>
    <p class="raffle-items">TV's, Digital Mixing Consoles, Speakers and Items Valued at</p>
    <p class="raffle-value">$25,000.</p>
    <p class="hours">930am-230pm</p>
    <p class="venue-address">KTR Warehouse 4920 County Rd 38<br>Cedar Bend AL 35990</p>
  </section>

  <div class="mixer-photo" role="img" aria-label="Large digital mixing console"></div>
  <p class="mixer-caption">Digital Mixers QX-48 Stage</p>

  <footer class="footer-brand">
    <p class="footer-name">KTR</p>
    <p class="footer-web">www.ktrworks-demo.net</p>
  </footer>
</main>
</body>
</html>
```